Marlowe Crest Salon needs a product poster

This poster is advertising our products and services. There are several damask patterns throughout the store. Our store's colors are blue, yellow, white, and gold.However the use of vibrant colors would be great! Our theme is old Hollywood. We have to use this design for our price list, product advertisement, and store promotions poster. Poster 2 and 3 can have the same layout. Poster 1 is different because I want the menu enclosed in a frame with the model resting against it or on top of it. All three posters will be hung on the same wall. I have attached my logo and additional photos for your review. I have also attached a images few posters. To give a better idea. I like how the fonts are not all the same. I like how they used the space. I like the use of color. Also I want the logo small with a white oval background. I don't want our logo to be a focal point.
Poster 1: The menu. This poster should include the blonde sailor either above the menu or beside the menu, 2 images have been included to choose from. I want the area with the prices in some type of decorative frame, with the model on top or on the side. (The model is displaying the prices) Also the model's background is white but I want her background to have color. Green would be great! I also like the idea of having "Now Showing" as part of the frame.
The text should read
" Services
Full Body Application..........................................$35.00
Half Body Application.........................................$20.00
Competition Application......................................$50,00
Face Only...........................................................$10.00
Packages:
4 Tans.... ............................................................$120.00 (Never Expires)
8 Tans ................................................................$200.00 (Never Expires)
Monthly Unlimited...............................................$95.00
Specials:
High School Students .......................................$25.00 EVERYDAY!!
All Day Every Tuesday.......................................$25.00
New Clients........................................................$25.00 (First Visit Only)
(If you want to be creative this section can be separate from the menu or part of the menu. Your choice)
Don't have time to come to us? We also have MOBILE Services! OUR ARTISTS CAN COME TO YOU!
In-Home Party Rates (5 people or more)...........$35.00 per person (Travel Fee Waived)
Poster 2: Rapid Solution...The image of the pinup with the clock if for this poster.
The text should read:
" PRESSED FOR TIME? Try our RAPID sunless solution. Rinse in as little as 2 hours" (Pressed for time, Rapid, and 2 Hours is what we want to stand out)
Poster 3: Packages..The image for this poster is of the girl with the binoculars.
The text should read:
"We offer packages and memberships with UNBELIEVABLE SAVINGS. Tans as low as $20!!" (Unbelievable savings and $20 is what we want to stand out)
Updates
I made changes to my briefing. Please let me know if I need to make any other changes or additions
We increased our budget for our design, in order to get more participants
I updated our brief. I have included examples and more detailed instructions. I hope this helps
Target Market(s)
People who value beauty and glamour. We have an upscale clientele.
Industry/Entity Type
Advertising

```html
<!DOCTYPE html>
<html lang="en">
<head>
<meta charset="utf-8">
<title>Marlowe Crest Salon – Price List</title>
<link rel="stylesheet" href="https://fonts.googleapis.com/css2?family=Lobster&family=Abril+Fatface&display=swap">
<style>
  :root {
    --frame-black: #0b0b0b;
    --stripe-navy: #4a4f7a;
    --stripe-cream: #ece6d6;
    --panel-orange: #f5a321;
    --panel-inner: #fbbd3a;
    --sprocket: #fcc451;
    --ink: #1c2f3b;
    --model-light: #efe6d0;
    --model-mid: #c9a57c;
    --model-shadow: #3a2a1c;
  }
  * { box-sizing: border-box; margin: 0; padding: 0; }
  html, body { width: 957px; height: 1200px; overflow: hidden; background: var(--frame-black); }
  .poster { position: relative; width: 957px; height: 1200px; background: var(--frame-black); overflow: hidden; }
  .stripes {
    position: absolute; left: 21px; top: 22px; width: 915px; height: 1159px;
    background: repeating-linear-gradient(90deg, var(--stripe-cream) 0 18px, var(--stripe-navy) 18px 36px);
  }
  .film-panel { position: absolute; left: 287px; top: 48px; width: 617px; height: 1111px; background: var(--panel-orange); }
  .film-panel .inner { position: absolute; left: 106px; top: 26px; width: 425px; height: 1053px; background: var(--panel-inner); border-radius: 22px; }
  .sprocket { position: absolute; width: 46px; height: 50px; background: var(--sprocket); border-radius: 8px; }
  .brand {
    position: absolute; left: 32px; top: 66px;
    font-family: "Lobster", cursive; font-size: 30px; color: var(--ink);
  }
  .model-photo {
    position: absolute; left: 0; top: 181px; width: 393px; height: 946px;
    background: linear-gradient(90deg, var(--model-light) 0%, var(--model-mid) 70%, var(--model-shadow) 100%);
    border-radius: 120px 60px 0 0;
  }
  .menu { position: absolute; left: 399px; width: 418px; font-family: "Lobster", cursive; color: var(--ink); }
  .heading { position: absolute; right: 0; font-size: 27px; white-space: nowrap; }
  .row { position: absolute; right: 0; display: flex; align-items: baseline; font-size: 18px; white-space: nowrap; }
  .row .dots { flex: 1; border-bottom: 2px dotted var(--ink); margin: 0 2px; transform: translateY(-4px); }
  .note { position: absolute; right: 0; font-size: 18px; white-space: nowrap; }
  .mobile-callout {
    position: absolute; right: 140px; top: 860px; text-align: right;
    font-family: "Abril Fatface", serif; font-size: 32px; line-height: 43px; color: var(--ink); white-space: nowrap;
  }
  .party { position: absolute; right: 140px; text-align: right; font-family: "Lobster", cursive; font-size: 18px; color: var(--ink); white-space: nowrap; }
</style>
</head>
<body>
<div class="poster">
  <div class="stripes"></div>

  <div class="film-panel">
    <div class="sprocket" style="left:18px;top:60px"></div>
    <div class="sprocket" style="left:18px;top:190px"></div>
    <div class="sprocket" style="left:18px;top:320px"></div>
    <div class="sprocket" style="left:18px;top:450px"></div>
    <div class="sprocket" style="left:18px;top:580px"></div>
    <div class="sprocket" style="left:18px;top:710px"></div>
    <div class="sprocket" style="left:18px;top:840px"></div>
    <div class="sprocket" style="left:18px;top:970px"></div>
    <div class="sprocket" style="left:548px;top:60px"></div>
    <div class="sprocket" style="left:548px;top:190px"></div>
    <div class="sprocket" style="left:548px;top:320px"></div>
    <div class="sprocket" style="left:548px;top:450px"></div>
    <div class="sprocket" style="left:548px;top:580px"></div>
    <div class="sprocket" style="left:548px;top:710px"></div>
    <div class="sprocket" style="left:548px;top:840px"></div>
    <div class="sprocket" style="left:548px;top:970px"></div>
    <div class="inner"></div>
  </div>

  <div class="brand">Marlowe Crest Salon</div>

  <div class="model-photo" role="img" aria-label="Photo of a blonde pin-up model in a white sailor dress and anchor cap, hand on hip, with a dark cut-out shadow behind her"></div>

  <div class="menu" style="top:0">
    <div class="heading" style="top:96px">Services</div>
    <div class="row" style="top:170px;width:418px"><span>Full Body Application</span><span class="dots"></span><span>$35.00</span></div>
    <div class="row" style="top:200px;width:418px"><span>Half Body Application</span><span class="dots"></span><span>$20.00</span></div>
    <div class="row" style="top:229px;width:418px"><span>Competition Application</span><span class="dots"></span><span>$50,00</span></div>
    <div class="row" style="top:259px;width:418px"><span>Face Only</span><span class="dots"></span><span>$10.00</span></div>

    <div class="heading" style="top:325px">Packages:</div>
    <div class="row" style="top:391px;width:379px"><span>4 Tans</span><span class="dots"></span><span>$120.00</span></div>
    <div class="note" style="top:423px">( Never Expires )</div>
    <div class="row" style="top:452px;width:379px"><span>8 Tans</span><span class="dots"></span><span>$200.00</span></div>
    <div class="note" style="top:482px">( Never Expires )</div>
    <div class="row" style="top:512px;width:379px"><span>Monthly Unlimited</span><span class="dots"></span><span>$95.00</span></div>

    <div class="heading" style="top:577px">Specials:</div>
    <div class="row" style="top:644px;width:269px"><span>High School Students</span><span class="dots"></span><span>$25.00</span></div>
    <div class="note" style="top:674px">(Everyday)</div>
    <div class="row" style="top:705px;width:269px"><span>All Day Every Tuesday</span><span class="dots"></span><span>$25.00</span></div>
    <div class="row" style="top:737px;width:269px"><span>New Clients</span><span class="dots"></span><span>$25.00</span></div>
    <div class="note" style="top:766px">(First Visit Only)</div>
  </div>

  <div class="mobile-callout">
    DON T HAVE TIME TO COME<br>
    TO US&nbsp; WE ALSO HAVE<br>
    MOBILE SERVICES&nbsp; OUR<br>
    ARTISTS CAN COME TO YOU
  </div>

  <div class="party" style="top:1061px">In-Home Party Rates (5 people or more)....$35.00</div>
  <div class="party" style="top:1091px">per person (Travel Fee Waived)</div>
</div>
</body>
</html>
```